Consulting company, design, Interior design in commercial real estate (Tertiai sector *

Company name: DORALYNE: from the Greek Evexia well-being, was born from a desire to combine well-being and work. By the choice of design, materials, design and furniture, everything is thought from this perspective

Logo: Essay with Möbius Ribbon and / or with the infinite acronym / and or triangle ...
Sentences to write:
"The exclusive partner for your development projects"
"Consulting - Design - Construction"
"We manage EVERYTHING for you"

On the back: Photo (attached; if photo is not clear, another photo can be provided) with company name and "DORALYNE, Excellence and reliability"
My name / First name: provided later (double name), Manager
Address: supplied later
Tel: supplied later
Website: www. doralyne.example
Colors: Black, gold and white. Other admissible colors
See attached files

Target Market(s)

Real estate business

Contact Information for Business Card

Nom de l'entreprise : DORALYNE : du grec Evexia bien être, est né d'une volonté de faire rimer bien être et travail. Par le choix de la conception, des matériaux, du design et du mobilier, tout est pensé dans cette optique

Logo : Essai avec Ruban de Möbius et /ou avec le sigle infini / et ou triangle...
Phrases à inscrire :
"Le partenaire exclusif de vos projets d'aménagement"
"Conseil - Conception - Construction"
"Nous gérons TOUT pour vous"

Au verso : Photo (ci-jointe ; si photo pas nette, une autre photo peut être fournie) avec nom de l'entreprise et Mention "DORALYNE, Excellence et fiabilité"
Mon nom / Prénom : fourni ultérieurement (prénom double), Gérant
Adresse : fourni ultérieurement
Tél : fourni ultérieurement
Site Web : www. doralyne.example
Couleurs : Noir, doré et blanc. Autre couleurs recevables
Voir fichiers ci-joint

Requirements
Must have
• My project must be simple, clear, neat and design.
The business card must catch the customer

```html
<!DOCTYPE html>
<html lang="fr">
<head>
<meta charset="utf-8">
<title>DORALYNE – Carte de visite</title>
<link href="https://fonts.googleapis.com/css2?family=Poppins:wght@300;400;500;600;700&display=swap" rel="stylesheet">
<style>
  :root {
    --black: #000000;
    --white: #ffffff;
    --ink: #111111;
    --stage: #ece9e4;
    --gold-dark: #b5832a;
    --gold-mid: #d9b24a;
    --gold-light: #f6e482;
    --gold-gradient: linear-gradient(180deg, #b5832a 0%, #d7ab3f 35%, #f6e482 70%, #e2c25a 100%);
    --gold-gradient-h: linear-gradient(90deg, #c4922e 0%, #e8cc5c 30%, #f8e98c 55%, #d6a93c 80%, #b9872b 100%);
    --photo-tone: radial-gradient(circle at 50% 40%, #b9bcc3 0%, #9da1a9 55%, #6f737b 100%);
  }
  * { margin: 0; padding: 0; box-sizing: border-box; }
  html, body { width: 1189px; height: 1200px; overflow: hidden; }
  body {
    background: var(--stage);
    font-family: "Poppins", sans-serif;
    position: relative;
  }

  .card {
    position: absolute;
    top: 218px;
    width: 437px;
    height: 764px;
    overflow: hidden;
    box-shadow: 0 6px 18px rgba(0,0,0,0.25);
  }

  /* ---------- Front ---------- */
  .card--front { left: 148px; background: var(--black); }

  .front__panel { position: absolute; left: 0; top: 0; width: 365px; height: 100%; }

  .headline {
    position: absolute; top: 78px; left: 0; width: 100%;
    text-align: center; color: var(--white);
    font-weight: 300; font-size: 32px; letter-spacing: 3.5px; line-height: 41px;
  }
  .headline__accent { color: var(--gold-mid); font-weight: 600; letter-spacing: 1px; }

  .promise {
    position: absolute; top: 262px; left: 0; width: 100%;
    text-align: center; color: var(--white);
    font-weight: 500; font-size: 16.5px; letter-spacing: 1.4px; line-height: 30.5px;
  }

  .brand {
    position: absolute; top: 560px; left: 0; width: 100%;
    text-align: center; color: var(--gold-mid);
  }
  .brand__mark {
    width: 40px; height: 40px; margin: 0 auto 38px;
    background: var(--gold-mid);
  }
  .brand__name {
    font-weight: 500; font-size: 37px; letter-spacing: 6px; line-height: 40px;
    color: var(--white);
  }
  .brand__tagline {
    margin-top: 4px;
    font-weight: 500; font-size: 11.5px; letter-spacing: 2.2px;
    color: var(--white);
  }

  .front__rule {
    position: absolute; top: 0; left: 365px; width: 5px; height: 100%;
    background: var(--white);
  }
  .front__band {
    position: absolute; top: 0; left: 375px; width: 62px; height: 100%;
    background: var(--gold-gradient);
    display: flex; align-items: center; justify-content: center;
  }
  .front__band-text {
    writing-mode: vertical-rl; transform: rotate(180deg);
    font-weight: 500; font-size: 18px; letter-spacing: 4.2px;
    color: var(--ink); white-space: nowrap;
  }

  /* ---------- Back ---------- */
  .card--back { left: 604px; background: var(--white); }

  .portrait {
    position: absolute; left: 101px; top: 57px; width: 234px; height: 234px;
    border-radius: 50%;
    background: var(--gold-gradient);
    padding: 5px;
  }
  .portrait__photo {
    width: 100%; height: 100%; border-radius: 50%;
    background: var(--photo-tone);
  }

  .identity {
    position: absolute; top: 326px; left: 0; width: 100%;
    text-align: center; color: var(--ink);
  }
  .identity__name { font-size: 20.5px; letter-spacing: 0.3px; line-height: 30px; }
  .identity__first { font-weight: 700; }
  .identity__last { font-weight: 400; }
  .identity__role { font-weight: 400; font-size: 15px; letter-spacing: 2px; line-height: 22px; }

  .contact-divider {
    position: absolute; left: 83px; width: 272px; height: 28px;
    display: flex; align-items: center; gap: 6px;
  }
  .contact-divider__line {
    flex: 1; height: 1.5px;
    background: linear-gradient(90deg, rgba(201,154,46,0), var(--gold-dark) 40%, var(--gold-mid));
  }
  .contact-divider__line--right {
    background: linear-gradient(90deg, var(--gold-mid), var(--gold-dark) 60%, rgba(201,154,46,0));
  }
  .contact-divider__icon {
    width: 28px; height: 28px; border-radius: 50%;
    background: var(--gold-gradient);
    border: 2px solid var(--gold-dark);
    display: flex; align-items: center; justify-content: center;
  }
  .contact-divider__icon svg { width: 15px; height: 15px; }

  .contact-text {
    position: absolute; left: 0; width: 100%;
    text-align: center; color: var(--ink);
    font-weight: 400; font-size: 20px; letter-spacing: 0.4px;
  }
  .contact-text--address { font-size: 17px; line-height: 28px; letter-spacing: 0.2px; }

  .back__rule {
    position: absolute; left: 0; top: 704px; width: 100%; height: 4px;
    background: var(--black);
  }
  .back__band {
    position: absolute; left: 0; top: 711px; width: 100%; height: 53px;
    background: var(--gold-gradient-h);
    display: flex; align-items: center; justify-content: center;
  }
  .back__website {
    font-weight: 500; font-size: 19px; letter-spacing: 3.2px; color: var(--ink);
  }
</style>
</head>
<body>

  <section class="card card--front" aria-label="Recto">
    <div class="front__panel">
      <h1 class="headline">NOUS GÉRONS<br><span class="headline__accent">TOUT</span><br>POUR VOUS</h1>
      <p class="promise">LE PARTENAIRE EXCLUSIF<br>DE VOS<br>PROJETS D'AMÉNAGEMENT</p>
      <div class="brand">
        <div class="brand__mark"></div>
        <div class="brand__name">DORALYNE</div>
        <div class="brand__tagline">EXCELLENCE ET FIABILITÉ</div>
      </div>
    </div>
    <div class="front__rule"></div>
    <div class="front__band">
      <span class="front__band-text">CONSEIL - CONCEPTION - RÉALISATION</span>
    </div>
  </section>

  <section class="card card--back" aria-label="Verso">
    <div class="portrait">
      <div class="portrait__photo" role="img" aria-label="Portrait photo of the manager"></div>
    </div>

    <div class="identity">
      <div class="identity__name"><span class="identity__first">MARC-ANTOINE</span> <span class="identity__last">LEFÉBURE</span></div>
      <div class="identity__role">GÉRANT</div>
    </div>

    <div class="contact-divider" style="top:414px">
      <span class="contact-divider__line"></span>
      <span class="contact-divider__icon">
        <svg viewBox="0 0 24 24" fill="none" stroke="#ffffff" stroke-width="2" stroke-linecap="round" stroke-linejoin="round"><path d="M5 3h4l2 5-2.5 1.5a11 11 0 0 0 6 6L16 13l5 2v4a2 2 0 0 1-2 2A16 16 0 0 1 3 5a2 2 0 0 1 2-2z"/></svg>
      </span>
      <span class="contact-divider__line contact-divider__line--right"></span>
    </div>
    <p class="contact-text" style="top:447px">06 12 47 90 35</p>

    <div class="contact-divider" style="top:488px">
      <span class="contact-divider__line"></span>
      <span class="contact-divider__icon">
        <svg viewBox="0 0 24 24" fill="none" stroke="#ffffff" stroke-width="2" stroke-linejoin="round"><rect x="3" y="6" width="18" height="12" rx="1"/><path d="M3 7l9 6 9-6"/></svg>
      </span>
      <span class="contact-divider__line contact-divider__line--right"></span>
    </div>
    <p class="contact-text" style="top:520px">contact@doralyne.example</p>

    <div class="contact-divider" style="top:561px">
      <span class="contact-divider__line"></span>
      <span class="contact-divider__icon">
        <svg viewBox="0 0 24 24" fill="none" stroke="#ffffff" stroke-width="2" stroke-linejoin="round"><path d="M12 22s7-7 7-12a7 7 0 0 0-14 0c0 5 7 12 7 12z"/><circle cx="12" cy="10" r="2.5"/></svg>
      </span>
      <span class="contact-divider__line contact-divider__line--right"></span>
    </div>
    <p class="contact-text contact-text--address" style="top:597px">14 Allée des Tilleuls<br>01250 Ste MARIE SUR VEYLE</p>

    <div class="back__rule"></div>
    <div class="back__band">
      <span class="back__website">www.doralyne.example</span>
    </div>
  </section>

</body>
</html>
```